A5 Flyer for Financial Services Business

I am after a re-design of our business flyer to fit in with our new branding style and logo colour scheme. Wanting something with a bit of designer flair that I could not create myself. I have included the flyer which I created which lacks style so dazzle me.

I want to use the same content.

Text for main body of flyer is

Are you a small business owner, tradie or PAVC Service Provider struggling to stay on top of your bookkeeping and compliance obligations? If so we would love to help you get back on track and take control of your business finances so that you can make informed business decisions and focus on what you do best.

We have over 20 years industry experience and, as a small business ourselves, we are able to offer our clients a personal bookkeeping solution tailored to meet the needs of your business.

Accounts Payable | Accounts Receivable
Customer Invoicing
Bank and Credit Card Reconciliations
Payroll | Superannuation | Payroll Tax
Business Activity | Instalment Activity Statements
Regular Financial Reports
Ledgerly and BookNest Set-Up and Training

```html
<!DOCTYPE html>
<html lang="en">
<head>
<meta charset="utf-8">
<title>Even Keel Financial Services – Bookkeeping Flyer</title>
<link rel="stylesheet" href="https://fonts.googleapis.com/css2?family=Oswald:wght@500&family=Montserrat:wght@400;700&family=Roboto:wght@700&family=Roboto+Condensed:wght@400&display=swap">
<style>
:root{
  --teal:#218f9c;
  --teal-bright:#22aea6;
  --teal-deep:#17707c;
  --ink:#3b3b3b;
  --paper:#fbfbfb;
  --white:#ffffff;
  --lime:#c9d93a;
}
*{margin:0;padding:0;box-sizing:border-box}
html,body{width:900px;height:1200px;overflow:hidden;background:var(--paper)}
.flyer{position:relative;width:900px;height:1200px;overflow:hidden;background:var(--paper);font-family:'Montserrat',sans-serif;color:var(--ink)}

.hero-photo{position:absolute;left:39px;top:147px;width:821px;height:483px;
  background:linear-gradient(100deg,#c9d3d6 0%,#eef1f2 30%,#f3e6e3 55%,#e7eef5 78%,#bcd0e0 100%)}
.headline-box{position:absolute;left:80px;top:0;width:332px;height:371px;background:var(--teal);
  display:flex;align-items:center;justify-content:center;padding-top:30px}
.headline{font-family:'Oswald',sans-serif;font-weight:500;color:var(--white);font-size:52px;line-height:58px;text-align:center;letter-spacing:-0.5px}

.brand{position:absolute;left:560px;top:86px;width:300px;text-align:center;color:var(--teal);font-weight:400}
.brand-name{font-size:33px;letter-spacing:-1px;line-height:36px}
.brand-sub{font-size:15px;letter-spacing:6px;line-height:20px}

.content-panel{position:absolute;left:64px;top:527px;width:710px;height:110px;background:var(--paper)}
.intro{position:absolute;left:103px;width:632px;font-size:16.5px;line-height:30.5px;text-align:justify}
.intro-one{top:545px}
.intro-two{top:708px}
.intro strong{color:var(--teal);font-weight:700}

.services{position:absolute;top:0;width:0;height:0;list-style:none;font-family:'Roboto',sans-serif;font-weight:700;color:var(--teal-bright);font-size:19.5px;line-height:24px}
.services-left{left:119px}
.services-right{left:456px}
.service{position:absolute;left:0;display:flex;align-items:center;white-space:nowrap}
.service svg{width:19px;height:19px;margin-right:15px;flex:none}

.badge{position:absolute;left:770px;top:946px;width:104px;text-align:center;font-weight:700;font-size:12.5px;line-height:16px;color:var(--ink)}
.badge svg{display:block;margin:0 auto 4px}

.footer-band{position:absolute;left:0;top:1085px;width:900px;height:115px}
.credentials{position:absolute;left:28px;top:1107px;color:var(--white);font-weight:700;font-size:21px;line-height:34px;list-style:none}
.credentials li::before{content:"\25C6";margin-right:10px;font-size:17px}
.contact{position:absolute;left:522px;top:1100px;color:var(--white)}
.phone{display:flex;align-items:center;font-family:'Oswald',sans-serif;font-weight:500;font-size:52px;line-height:58px;letter-spacing:-0.5px}
.phone svg{width:46px;height:46px;margin-right:12px}
.web{font-family:'Roboto Condensed',sans-serif;font-size:21px;line-height:26px;margin-left:6px}
</style>
</head>
<body>
<main class="flyer">
  <div class="hero-photo" role="img" aria-label="Photo of two businesswomen reviewing finances at a laptop in a bright office"></div>

  <div class="headline-box">
    <h1 class="headline">BOOKKEEPING<br>TAILORED TO<br>YOUR BUSINESS<br>NEEDS</h1>
  </div>

  <div class="brand">
    <div class="brand-name">EVEN KEEL</div>
    <div class="brand-sub">Financial Services</div>
  </div>

  <div class="content-panel"></div>

  <p class="intro intro-one">Are you a small business owner, tradie or PAVC Service Provider struggling to stay on top of your bookkeeping and compliance obligations? If so we would love to help you get back on track and take control of your business finances so that you can make informed business decisions and focus on what you do best.</p>
  <p class="intro intro-two"><strong>We have over 20 years industry experience</strong> and, as a small business ourselves, we are able to offer our clients a personal bookkeeping solution tailored to meet the needs of your business.</p>

  <svg width="0" height="0" style="position:absolute" aria-hidden="true">
    <symbol id="tick-box" viewBox="0 0 20 20">
      <rect x="1.5" y="2.5" width="15" height="15" fill="none" stroke="#22aea6" stroke-width="2"/>
      <path d="M5 9.5l4 4L18.5 2" fill="none" stroke="#22aea6" stroke-width="2.6" stroke-linecap="round" stroke-linejoin="round"/>
    </symbol>
  </svg>

  <ul class="services services-left">
    <li class="service" style="top:822px"><svg><use href="#tick-box"/></svg>ACCOUNTS PAYABLE</li>
    <li class="service" style="top:860px"><svg><use href="#tick-box"/></svg>ACCOUNTS RECEIVABLE</li>
    <li class="service" style="top:898px"><svg><use href="#tick-box"/></svg>CUSTOMER INVOICING</li>
    <li class="service" style="top:933px"><svg><use href="#tick-box"/></svg><span>BANK AND CREDIT CARD<br>RECONCILIATIONS</span></li>
    <li class="service" style="top:992px"><svg><use href="#tick-box"/></svg>PAYROLL</li>
    <li class="service" style="top:1027px"><svg><use href="#tick-box"/></svg>SUPERANNUATION</li>
  </ul>

  <ul class="services services-right">
    <li class="service" style="top:822px"><svg><use href="#tick-box"/></svg>PAYROLL TAX</li>
    <li class="service" style="top:860px"><svg><use href="#tick-box"/></svg>BUSINESS ACTIVITY</li>
    <li class="service" style="top:896px"><svg><use href="#tick-box"/></svg><span>INSTALMENT ACTIVITY<br>STATEMENTS</span></li>
    <li class="service" style="top:952px"><svg><use href="#tick-box"/></svg><span>REGULAR FINANCIAL<br>REPORTS</span></li>
    <li class="service" style="top:1011px"><svg><use href="#tick-box"/></svg><span>LEDGERLY AND BOOKNEST<br>SET-UP AND TRAINING</span></li>
  </ul>

  <div class="badge">
    <svg width="100" height="100" viewBox="0 0 100 100" aria-hidden="true">
      <circle cx="50" cy="50" r="47" fill="#fff" stroke="#3b3b3b" stroke-width="1.5"/>
      <circle cx="50" cy="50" r="27" fill="#c9d93a"/>
    </svg>
    BAS Agent<br>12345678
  </div>

  <svg class="footer-band" viewBox="0 0 900 115" preserveAspectRatio="none" aria-hidden="true">
    <defs>
      <linearGradient id="band-shade" x1="0" x2="1">
        <stop offset="0" stop-color="#17707c"/>
        <stop offset="1" stop-color="#218f9c"/>
      </linearGradient>
    </defs>
    <polygon points="370,0 900,0 900,115 510,115" fill="#22aea6"/>
    <polygon points="0,10 420,10 505,115 505,105 0,105" fill="#22aea6"/>
    <polygon points="370,0 420,10 505,105 520,115 505,115 420,15" fill="url(#band-shade)"/>
    <polygon points="360,10 420,10 500,105 440,105" fill="url(#band-shade)" opacity="0.55"/>
  </svg>

  <ul class="credentials">
    <li>LEDGERLY CERTIFIED ADVISOR</li>
    <li>BOOKNEST PRO PARTNER</li>
  </ul>

  <div class="contact">
    <div class="phone">
      <svg viewBox="0 0 46 46" aria-hidden="true">
        <rect x="2" y="2" width="42" height="42" rx="10" fill="#fff"/>
        <path d="M15 11c2 0 4 5 4 6s-2 2-2 3c1 3 4 7 8 8 1 0 2-2 3-2s6 2 6 4-2 5-5 5c-9 0-17-8-17-17 0-3 2-7 3-7z" fill="#22aea6"/>
        <path d="M27 12a8 8 0 0 1 7 7M27 7a13 13 0 0 1 12 12" fill="none" stroke="#22aea6" stroke-width="2.2" stroke-linecap="round"/>
      </svg>
      0400 123 456
    </div>
    <div class="web">evenkeelfinancial.com.au</div>
  </div>
</main>
</body>
</html>
```